Kettlebrook Holdings, LLC. What we do is rehab homes for the purpose of flipping them and also have a rental portfolio as well.

We do not have a logo so that will need to be part of the design process

Would like, if possible to have a house or something with housing or remodeling incorporated in design.

Industry/Entity Type

Rental

Contact Information for Business Card

Dale Varnum
912 thistle Ct.
Fernhollow, il 60199
847-555-0143
Fax 630-555-0178

```html
<!DOCTYPE html>
<html lang="en">
<head>
<meta charset="utf-8">
<title>Kettlebrook Holdings, LLC — Business Card</title>
<link href="https://fonts.googleapis.com/css2?family=Arimo:wght@400;500&display=swap" rel="stylesheet">
<style>
  :root {
    --page-bg: #e4e4e4;
    --card-white: #ffffff;
    --ink: #111111;
    --band-black: #0a0a0a;
    --gold: #f2b51f;
  }
  html, body {
    margin: 0;
    padding: 0;
    width: 1200px;
    height: 857px;
    overflow: hidden;
    background: var(--page-bg);
    font-family: "Arimo", Arial, sans-serif;
  }
  .business-card {
    position: absolute;
    left: 170px;
    top: 157px;
    width: 860px;
    height: 542px;
    background: var(--card-white);
    border-radius: 34px;
    overflow: hidden;
    box-shadow: 0 18px 40px rgba(0,0,0,0.18);
  }
  .brand {
    position: absolute;
    top: 150px;
    left: 0;
    right: 0;
    display: flex;
    justify-content: center;
    align-items: center;
    gap: 16px;
  }
  .brand-mark {
    width: 34px;
    height: 34px;
    background: var(--gold);
  }
  .brand-name {
    font-size: 44px;
    font-weight: 500;
    color: var(--ink);
    letter-spacing: -0.5px;
    white-space: nowrap;
  }
  .contact-list {
    position: absolute;
    top: 262px;
    left: 0;
    right: 0;
    margin: 0;
    padding: 0;
    list-style: none;
    text-align: center;
    font-size: 19px;
    line-height: 29px;
    color: var(--ink);
  }
  .name-band {
    position: absolute;
    left: 0;
    right: 0;
    bottom: 0;
    height: 138px;
    background: var(--band-black);
    display: flex;
    align-items: center;
    justify-content: center;
  }
  .person-name {
    color: var(--gold);
    font-size: 34px;
    font-weight: 400;
    letter-spacing: -0.5px;
  }
</style>
</head>
<body>
  <article class="business-card">
    <div class="brand">
      <span class="brand-mark" aria-hidden="true"></span>
      <span class="brand-name">Kettlebrook Holdings, LLC.</span>
    </div>
    <ul class="contact-list">
      <li>phone : 847-555-0143</li>
      <li>fax : 630-555-0178</li>
      <li>Address : 912 thistle Ct. Fernhollow, il 60199</li>
    </ul>
    <div class="name-band">
      <span class="person-name">Dale Varnum</span>
    </div>
  </article>
</body>
</html>
```